I am seeking a book cover design for a new book series. The book deals with life and the principles and essentials that we must have in our lives in order to be happy and have a successful life. Some of the tenets will include 'Spirit' Believe' 'Trust' 'Harmony' 'Family' etc...

I would like to have some natural scene in the background (i.e. water, moutains, forest...that is a ZEN or purity feel)

The '24' should be pronounced in the title in within the foreground of the book cover.

I am open to colors but would like the coloring to emphasize attention. Colors such as forest greens, peaches, pomegranites, are ones that come to mind but i am completely open since it must fit the design.

I will also be looking to do a web design and other additional logos/designs in the coming months so this is a long term opportunity with the right design and communication. I look forward to working with a great partner on this project.

Project Deadline Extended
Reason: I am extending the deadline to allow designers who inquired to get their designs submitted. Also to allow several designers to submit changes to their design.

Target Market(s)

Spiritual - Age range 18-80 - Forward Thinkers - Degreed - All cultures and religions

Industry/Entity Type

Communication

Requirements
Must have
• The title 'The 17 Keystones of Being'

My Name as the Author: Dorian Pellwick

the thoughts should also include a backcover copy consistent with the front and a theme design for the Series.
The book is expected to be 5 1/2 x 8 1/2"
Nice to have
• The book will be released in a series format as well as the entire 17 Keystones. As a suggestion, the books released as part of an individual essential would have the name of that essential referenced on the book. Example (BELEIVE). You may take that into consideration when designing for he cover. Thank you.

```html
<!DOCTYPE html>
<html lang="en">
<head>
<meta charset="utf-8">
<title>The 17 Keystones of Being — Dorian Pellwick</title>
<link rel="stylesheet" href="https://fonts.googleapis.com/css2?family=Archivo+Black&family=Archivo:wdth,wght@62..125,700..800&display=swap">
<style>
  :root {
    --ink: #141414;
    --accent: #d8261c;
    --sky-top: #2f8fa6;
    --sky-mid: #7cc6cf;
    --cloud: #e3f1ee;
    --horizon: #f2f1b8;
    --hills: #4f7a52;
    --field-top: #8cc23f;
    --field-bottom: #4f9a22;
  }
  html, body {
    margin: 0;
    padding: 0;
    overflow: hidden;
    background: #ffffff;
  }
  .cover {
    position: relative;
    width: 776px;
    height: 1200px;
    overflow: hidden;
    font-family: "Archivo", Arial, sans-serif;
    color: var(--ink);
  }
  .scene {
    position: absolute;
    inset: 0;
    background:
      linear-gradient(180deg,
        var(--sky-top) 0%,
        var(--sky-mid) 14%,
        var(--cloud) 26%,
        var(--sky-mid) 38%,
        var(--cloud) 50%,
        var(--horizon) 63%,
        var(--hills) 66%,
        var(--hills) 68.5%,
        var(--field-top) 70.5%,
        var(--field-bottom) 100%);
  }
  .title {
    margin: 0;
    font-weight: normal;
  }
  .title-word {
    position: absolute;
    left: 40px;
    font-family: "Archivo Black", "Arial Black", sans-serif;
    line-height: 1;
    white-space: nowrap;
  }
  .title-the { top: 296px; left: 44px; font-size: 98px; letter-spacing: -4px; }
  .title-number { top: 376px; font-size: 156px; color: var(--accent); letter-spacing: -4px; }
  .title-keystones { top: 560px; font-size: 94px; letter-spacing: -1px; }
  .title-being { top: 640px; font-size: 94px; letter-spacing: -1px; }
  .keystone-list {
    position: absolute;
    left: 315px;
    top: 387px;
    margin: 0;
    padding: 0;
    list-style: none;
    font-weight: 700;
    font-stretch: 120%;
    font-size: 20px;
    line-height: 27px;
    white-space: nowrap;
  }
  .keystone-list .highlight { color: var(--accent); }
  .author {
    position: absolute;
    left: 40px;
    top: 754px;
    margin: 0;
    font-weight: 800;
    font-stretch: 110%;
    font-size: 33px;
    line-height: 1;
  }
</style>
</head>
<body>
  <main class="cover">
    <div class="scene" role="img" aria-label="Bright sky with clouds and a flock of birds over a green field with distant forested hills and an upholstered armchair standing in the grass"></div>

    <h1 class="title">
      <span class="title-word title-the">The</span>
      <span class="title-word title-number">17</span>
      <span class="title-word title-keystones">Keystones</span>
      <span class="title-word title-being">of Being</span>
    </h1>

    <ul class="keystone-list">
      <li>Believe - Courage - Destiny - Dream</li>
      <li>Faith - Family - Happiness - Harmony</li>
      <li>Health - Hope - Integrity - Love - Patience</li>
      <li>Peace - Prosperity - Respect - Serenity</li>
      <li>Spirit - Strength - Success - Trust - Truth</li>
      <li>Wisdom - <span class="highlight">You</span></li>
    </ul>

    <p class="author">Dorian Pellwick</p>
  </main>
</body>
</html>
```